Innovative Leadership Program Needs Flyer/Postcard to Quickly Convey Benefits

I am launching an innovative new 3-month leadership program for highly successful women professionals -- who also happen to be emotionally sensitive. This 4x6" postcard needs to convey a grounded, emotionally safe experience that's also revolutionary in it's discussion of emotions in the workplace. You'll find the style guide, text, and other elements in the attached detailed creative brief. POSTCARD is NOT for mailing. It's to be used to hand out at promotional events. DO NOT leave space for addressing. It's more like a flat flyer.

I polled a bunch of my clients. Fave image to use:https://files.quillmarrow.net/u/4815092/LeadershipFlyer/237415.jpg Added Monday, August 10, 2015

Target Market(s)

American professional women, largely Californian, 30-50 years old, work for big corporations in middle to senior management, more hip than the average business woman (not stuffy or ultra serious), into yoga or meditation or personal development.

Industry/Entity Type

Leadership

Font styles to use
Serif
Sans Serif

Colors
6b449b
f78f20
33a6d7

Requirements
Must have
• * Upbeat imagery. Somewhere between corporate but youthful/hip. Think of a 30-something at a Silicon Valley/San Francisco company.
• * Colors I shared in the Radiant Keelway Style Guide document (shows the RGB and CMYK colors that are part of my palette. You can use shades of these, too, with screening, etc) I can't really tell if the color palette on the PixelForum wheel true matches my computer with yours, so please see my attachments for my Style Guide for colors.
Nice to have
• iconography, infographics
Should not have
• Lots of heavy colors - please don't use much black or dark blue.
• You may not use my logo or copy for anything other than creating this project.

```html
<!DOCTYPE html>
<html lang="en">
<head>
<meta charset="utf-8">
<title>Radiant Keelway – Steadfast Self-Leadership Postcard</title>
<link href="https://fonts.googleapis.com/css2?family=Open+Sans:ital,wght@0,400;0,600;0,700;1,400&display=swap" rel="stylesheet">
<style>
  :root{
    --purple:#6b449b;
    --purple-light:#ece4f4;
    --orange:#f78f20;
    --orange-light:#fdf1e3;
    --blue:#33a6d7;
    --ink:#4a4a4a;
    --paper:#ffffff;
    --backdrop:#e9e4de;
  }
  *{box-sizing:border-box;margin:0;padding:0}
  html,body{width:889px;height:1200px;overflow:hidden}
  body{background:var(--backdrop);font-family:"Open Sans",Arial,sans-serif;color:var(--ink);position:relative}
  .card{position:absolute;left:66px;width:757px;height:530px;background:var(--paper);box-shadow:0 4px 14px rgba(0,0,0,.25);overflow:hidden}
  .card--front{top:40px}
  .card--back{top:630px}

  /* front */
  .brand{position:absolute;left:28px;top:24px;display:flex;align-items:center;gap:10px}
  .brand__dot{width:30px;height:30px;border-radius:50%;background:var(--purple)}
  .brand__name{font-size:26px;font-weight:600;color:var(--purple)}
  .rule{position:absolute;left:0;right:0;top:84px;height:10px;background:var(--purple)}
  .photo{position:absolute;background:linear-gradient(135deg,#d9cfc6,#a89b93 55%,#6f6a70)}
  .card--front .photo{left:0;top:94px;width:322px;height:286px}
  .intro{position:absolute;left:344px;top:110px;width:390px}
  .intro__title{font-size:25px;font-weight:700;color:var(--orange);line-height:1.2}
  .intro__lead{font-size:13.5px;line-height:1.45;margin-top:6px}
  .intro__dates{font-size:18px;font-weight:700;color:var(--orange);margin-top:16px}
  .intro__host{font-size:13px;margin-top:10px;line-height:1.45}
  .intro__host strong{font-size:15px;color:var(--purple)}
  .features{position:absolute;left:22px;right:22px;top:392px;display:flex;justify-content:space-between}
  .feature{width:130px;display:flex;gap:8px;align-items:flex-start}
  .feature__icon{flex:none;width:34px;height:34px;border-radius:50%;background:var(--orange);display:flex;align-items:center;justify-content:center}
  .feature__text{font-size:10px;line-height:1.3}
  .feature__text b{color:var(--purple);display:block;font-size:10.5px}
  .footer{position:absolute;left:0;right:0;bottom:0;height:38px;background:var(--purple);color:#fff;display:flex;align-items:center;justify-content:space-between;padding:0 24px;font-size:12px}
  .footer__contact{display:flex;gap:22px;align-items:center}

  /* back */
  .band{position:absolute;left:0;right:0;top:0;height:20px;background:var(--purple)}
  .card--back .photo{right:0;top:20px;width:250px;height:424px;background:linear-gradient(90deg,#ffffff,#ddd3cc 40%,#b3a7a0)}
  .details{position:absolute;left:40px;top:36px;width:450px;font-size:11.5px;line-height:1.45}
  .details__q{font-size:14px;font-weight:700;color:var(--purple);line-height:1.3;margin-bottom:6px}
  .details ul{list-style:none;margin:4px 0 10px}
  .details li{padding-left:16px;position:relative}
  .details li::before{content:"";position:absolute;left:2px;top:6px;width:7px;height:7px;border-radius:50%;background:var(--orange)}
  .details p{margin-bottom:8px}
  .details p strong{color:var(--purple)}
  .dates-band{position:absolute;left:0;right:0;bottom:38px;height:48px;background:var(--orange-light);color:var(--orange);font-size:18px;font-weight:700;display:flex;align-items:center;padding-left:40px}
</style>
</head>
<body>

<section class="card card--front">
  <div class="brand"><span class="brand__dot"></span><span class="brand__name">Radiant Keelway</span></div>
  <div class="rule"></div>
  <div class="photo" role="img" aria-label="Portrait of a smiling young professional woman in an office"></div>
  <div class="intro">
    <h1 class="intro__title">Steadfast Self-Leadership</h1>
    <p class="intro__lead">The revolutionary 3-month experience that empowers smart, emotionally sensitive women professionals to be strong and confident – in any business situation</p>
    <p class="intro__dates">September 12 – November 18, 2015</p>
    <p class="intro__host">Hosted by<br><strong>Dr. Mara Ellison</strong><br>Executive &amp; Leadership Coach</p>
  </div>
  <div class="features">
    <div class="feature">
      <span class="feature__icon"><svg width="18" height="18" viewBox="0 0 18 18"><rect x="2" y="4" width="14" height="12" rx="1" fill="none" stroke="#fff" stroke-width="2"/><line x1="2" y1="8" x2="16" y2="8" stroke="#fff" stroke-width="2"/></svg></span>
      <span class="feature__text"><b>Full Day Leadership Retreat</b>September 12, 2015</span>
    </div>
    <div class="feature">
      <span class="feature__icon"><svg width="18" height="18" viewBox="0 0 18 18"><circle cx="6" cy="6" r="3" fill="#fff"/><circle cx="12" cy="6" r="3" fill="#fff"/><path d="M1 16c0-4 3-5 5-5s5 1 5 5zM7 16c0-4 3-5 5-5s5 1 5 5z" fill="#fff"/></svg></span>
      <span class="feature__text"><b>6 Group Leadership Trainings</b>Live virtual sessions twice each month</span>
    </div>
    <div class="feature">
      <span class="feature__icon"><svg width="18" height="18" viewBox="0 0 18 18"><path d="M2 3h14v9H8l-4 3v-3H2z" fill="#fff"/></svg></span>
      <span class="feature__text"><b>3 One-on-One Coaching Sessions</b></span>
    </div>
    <div class="feature">
      <span class="feature__icon"><svg width="18" height="18" viewBox="0 0 18 18"><circle cx="9" cy="9" r="6" fill="none" stroke="#fff" stroke-width="2"/><circle cx="9" cy="9" r="2" fill="#fff"/></svg></span>
      <span class="feature__text"><b>Private Online Group</b>for 24/7 support</span>
    </div>
    <div class="feature">
      <span class="feature__icon"><svg width="18" height="18" viewBox="0 0 18 18"><rect x="2" y="7" width="14" height="9" fill="#fff"/><rect x="1" y="4" width="16" height="3" fill="#fff"/><line x1="9" y1="4" x2="9" y2="16" stroke="#f78f20" stroke-width="2"/></svg></span>
      <span class="feature__text"><b>Special Surprises</b></span>
    </div>
  </div>
  <footer class="footer">
    <span>Get all the details at</span>
    <span class="footer__contact"><span>www.radiantkeelway.com/lead</span><span>415-555-0136</span></span>
  </footer>
</section>

<section class="card card--back">
  <div class="band"></div>
  <div class="photo" role="img" aria-label="Confident businesswoman standing with arms folded"></div>
  <div class="details">
    <p class="details__q">You're likely an emotionally sensitive professional woman if you…</p>
    <ul>
      <li>frequently <strong>doubt yourself</strong></li>
      <li>wind up crying when you know it's not wise</li>
      <li>worry about how you're being perceived</li>
      <li>get angry or resentful when you're ignored or excluded</li>
      <li>often unsure about how to stand up for yourself</li>
      <li>feel the need to toughen up or become less sensitive</li>
    </ul>
    <p>Sensitivity is not a stigma. <strong>It's the most critical skill of the new economy.</strong> And it's in short supply. So when you harness the energy of your emotions, you're unstoppable.</p>
    <p><strong>Steadfast Self-Leadership is a 3-month experience that gives you one-on-one coaching, supportive community, plus proven tools and techniques so you can…</strong></p>
    <ul>
      <li>step up as the leader you're meant to be</li>
      <li>speak up for yourself, powerfully, even in confrontations</li>
      <li>stand up for what you believe and enthusiastically engage people</li>
      <li>manage your emotions so you feel more confident, relaxed, and natural</li>
      <li>respond gracefully, even when people around you are angry or upset</li>
      <li>be your authentic self at work</li>
    </ul>
  </div>
  <div class="dates-band">September 12 – November 18, 2015</div>
  <footer class="footer">
    <span>Get all the details at</span>
    <span class="footer__contact"><span>www.radiantkeelway.com/lead</span><span>415-555-0136</span></span>
  </footer>
</section>

</body>
</html>
```